CoverLantern.com website re-design - modern engaging website creation

We have an existing website. Www.CoverLantern.com - the content on the site and our widgets are custom built. But the layout and design of our site we just put there as we built the functionality around it. We want a new, bold, and modern design aimed at getting visitors to run a life insurance quote and ultimately apply. Our demographic is centered around those between the ages of 30-60. So we are looking at a complete site overhaul with better pictures, buttons, and an extremely modern design.

Target Market(s)

30-50 year olds

Industry/Entity Type

Life insurance

Coding

Coded - Design and coding required

Number of Pages Required

5+ page

Font styles to use
Other font styles liked:
• Rubik

Colors
0054AA
0677BA
7BADD7
CADEEF
E8F1F8
00AB8E
00BBA5
67D7C9
C6EFE9
E9F9F6
59FF00
82FF00
B8FF75
E3FFCB
F4FFEA

Requirements
Must have
• Matching color schemes from existing website. We have custom widgets on our site now and those must be . White space is important to make it simple for the user to navigate
Nice to have
• Same content - different more modern design
Should not have
• Colors outside of our current color scheme. Should NOT be too similar to our existing site.

```html
<!DOCTYPE html>
<html lang="en">
<head>
<meta charset="utf-8">
<title>CoverLantern – Life Insurance Online</title>
<link rel="stylesheet" href="https://fonts.googleapis.com/css2?family=Poppins:wght@300;400;500;600;700;800&display=swap">
<style>
:root{
  --blue:#2a7bc0;
  --blue-dark:#0677ba;
  --green:#7fc242;
  --ink:#1a1a1a;
  --muted:#6b6f75;
  --text:#3d4046;
  --header:#2b2b2b;
  --soft:#eff4f9;
  --white:#ffffff;
}
*{box-sizing:border-box;margin:0;padding:0}
html,body{width:1200px;height:3770px;overflow:hidden}
body{position:relative;font-family:'Poppins',sans-serif;color:var(--text);background:var(--white)}
.abs{position:absolute}
.btn{position:absolute;display:flex;align-items:center;justify-content:center;font-weight:600;font-size:11px;letter-spacing:.2px;color:var(--white);background:var(--green);border-radius:3px;text-transform:uppercase}
.btn.blue{background:var(--blue)}
.site-header{position:absolute;left:0;top:0;width:1200px;height:117px;background:var(--header)}
.top-link{position:absolute;top:0;height:24px;display:flex;align-items:center;justify-content:center;font-size:10px;font-weight:600;color:var(--white);border-radius:0 0 8px 8px;text-transform:uppercase}
.top-link.apply{left:654px;width:161px;background:var(--blue)}
.top-link.login{left:827px;width:162px;background:var(--green)}
.brand{position:absolute;font-weight:300;color:var(--white);letter-spacing:-.3px}
.site-header .brand{left:209px;top:50px;font-size:30px;line-height:1}
.main-nav{position:absolute;top:59px;left:524px}
.main-nav a{position:absolute;white-space:nowrap;font-size:11px;font-weight:600;color:var(--white);text-decoration:none}
.hero-art{position:absolute;left:0;top:117px}
.hero-copy{position:absolute;left:209px;top:244px;color:var(--white)}
.eyebrow{font-size:14px;font-weight:600;letter-spacing:4.6px}
.hero-title{margin-top:20px;font-size:51px;line-height:60px;font-weight:700}
.hero-title .light{font-weight:300}
.hero-lead{margin-top:14px;font-size:12.5px;line-height:21px;width:400px}
.carrier{position:absolute;top:834px;font-weight:600;font-size:18px;color:#3c3c3c;transform:translateX(-50%);white-space:nowrap}
.divider{position:absolute;left:176px;top:933px;width:848px;height:1px;background:#dcdcdc}
.section-title{position:absolute;font-size:29px;font-weight:700;color:var(--ink);letter-spacing:-.2px;line-height:1}
.section-text{position:absolute;font-size:12px;line-height:21px;color:var(--muted)}
.ticks{position:absolute;list-style:none}
.ticks li{position:relative;padding-left:24px;font-size:15px;line-height:21px;color:var(--text)}
.ticks li::before{content:"";position:absolute;left:0;top:5px;width:12px;height:12px;border-radius:50%;background:var(--blue)}
.ticks li::after{content:"";position:absolute;left:4px;top:7.5px;width:3px;height:5.5px;border:solid var(--white);border-width:0 1.6px 1.6px 0;transform:rotate(45deg)}
.ticks.on-blue li{color:var(--white)}
.ticks.on-blue li::before{background:var(--white)}
.ticks.on-blue li::after{border-color:var(--blue)}
.compare-band{position:absolute;left:0;top:1397px;width:1200px;height:486px;background:var(--blue)}
.compare-band .section-title{color:var(--white)}
.quote-card{position:absolute;width:218px;height:75px;background:var(--white);border-radius:4px;display:flex;align-items:center;padding:0 14px}
.quote-card .name{font-size:14px;font-weight:600;color:#333;width:100px;text-align:center}
.quote-card .terms{flex:1;text-align:center;font-size:6.5px;line-height:13px;color:#777}
.quote-card .price{font-size:19px;font-weight:700;color:#222;line-height:1.2}
.quote-card .price sup{font-size:9px}
.quote-card .price small{font-size:7px;font-weight:600}
.live-band{position:absolute;left:0;top:2377px;width:1200px;height:471px;background:var(--soft)}
.footer-art{position:absolute;left:0;top:3180px}
.footer-col{position:absolute;color:var(--white)}
.footer-col h4{font-size:20px;font-weight:600;margin-bottom:18px;line-height:1}
.footer-col ul{list-style:none}
.footer-col li{position:relative;padding-left:22px;font-size:15.5px;line-height:33px;white-space:nowrap}
.footer-col li svg{position:absolute;left:0;top:11px}
.footer-rule{position:absolute;left:124px;top:3709px;width:932px;height:1px;background:rgba(255,255,255,.55)}
.copyright{position:absolute;left:0;top:3733px;width:1200px;text-align:center;font-size:13px;color:var(--white)}
.social{position:absolute;top:3581px;width:18px;height:18px;border-radius:50%;border:2px solid var(--white)}
</style>
</head>
<body>

<header class="site-header">
  <a class="top-link apply">Continue Application</a>
  <a class="top-link login">Existing Client Login</a>
  <div class="brand">CoverLantern</div>
  <nav class="main-nav">
    <a style="left:0">FREE QUOTE</a>
    <a style="left:101px">NO EXAM</a>
    <a style="left:187px">ARTICLES</a>
    <a style="left:272px">FAQ'S</a>
    <a style="left:336px">ABOUT</a>
    <a style="left:408px">CONTACT</a>
  </nav>
</header>

<svg class="hero-art" width="1200" height="630" viewBox="0 117 1200 630">
  <defs>
    <linearGradient id="heroPhoto" x1="0" y1="0" x2="1" y2="0.35">
      <stop offset="0" stop-color="#c9a98a"/>
      <stop offset="0.2" stop-color="#6f6a55"/>
      <stop offset="0.42" stop-color="#4c5038"/>
      <stop offset="0.62" stop-color="#c98a3e"/>
      <stop offset="0.8" stop-color="#8a5a2c"/>
      <stop offset="1" stop-color="#33381f"/>
    </linearGradient>
  </defs>
  <path d="M0,630 C320,790 820,780 1200,600 V117 H0 Z" fill="var(--blue)"/>
  <path role="img" aria-label="Photo of a smiling family walking along a sunlit forest lakeside, father carrying his son on his back" d="M0,117 H1200 V585 C820,720 340,720 0,638 Z" fill="url(#heroPhoto)"/>
</svg>

<div class="hero-copy">
  <div class="eyebrow">WELCOME TO COVER LANTERN</div>
  <h1 class="hero-title">Cover Lantern<br><span class="light">Makes You The</span><br>Insurance Agent</h1>
  <p class="hero-lead">Lorem ipsum dolor sit amet, consectetur adipiscing elit, sed do eiusmod tempor incididunt ut labore et dolore magna aliqua.</p>
</div>
<a class="btn" style="left:212px;top:538px;width:126px;height:41px">Get Started</a>
<a class="btn" style="left:345px;top:538px;width:47px;height:41px;background:var(--white)">
  <svg width="8" height="9" viewBox="0 0 8 9"><path d="M1,0.5 L7,4.5 L1,8.5 Z" fill="var(--blue)"/></svg>
</a>

<div class="carrier" style="left:231px">Northvale</div>
<div class="carrier" style="left:383px">Plainsmark</div>
<div class="carrier" style="left:547px">Crestline Life</div>
<div class="carrier" style="left:708px">Steadfast</div>
<div class="carrier" style="left:841px">Harborly</div>
<div class="carrier" style="left:980px">Keystead</div>
<div class="divider"></div>

<svg class="abs" style="left:200px;top:1000px" width="420" height="340" viewBox="0 0 420 340">
  <defs>
    <linearGradient id="couplePhoto" x1="0" y1="0" x2="1" y2="1">
      <stop offset="0" stop-color="#e8ddd0"/>
      <stop offset="0.45" stop-color="#8a6a52"/>
      <stop offset="0.75" stop-color="#4d6584"/>
      <stop offset="1" stop-color="#dfe2e6"/>
    </linearGradient>
  </defs>
  <path d="M40,100 C70,60 140,70 200,55 C280,35 360,40 395,110 C420,170 410,220 385,250 C360,280 320,220 280,230 C200,250 120,220 80,190 C40,160 20,130 40,100 Z" fill="var(--blue)"/>
  <path role="img" aria-label="Photo of a smiling couple using a laptop at home" d="M60,125 C80,60 160,18 240,12 C320,8 360,70 358,150 C356,240 300,290 220,292 C140,294 70,260 48,210 C38,180 50,150 60,125 Z" fill="url(#couplePhoto)" stroke="var(--white)" stroke-width="6"/>
  <circle cx="113" cy="42" r="15" fill="var(--green)"/>
  <circle cx="142" cy="18" r="6" fill="var(--green)"/>
  <circle cx="346" cy="250" r="10" fill="var(--green)"/>
  <circle cx="253" cy="313" r="12" fill="var(--green)"/>
</svg>
<h2 class="section-title" style="left:640px;top:1060px">LIFE INSURANCE ONLINE</h2>
<p class="section-text" style="left:641px;top:1102px">Compare quotes from America's top insurance carriers<br>Pick your policy and apply in minutes</p>
<a class="btn" style="left:641px;top:1166px;width:155px;height:42px">Get Your Quote</a>

<section class="compare-band">
  <h2 class="section-title" style="left:117px;top:97px">COMPARE AND SAVE</h2>
  <ul class="ticks on-blue" style="left:117px;top:142px;width:395px">
    <li>Get Quotes without having to enter your contact information.</li>
    <li style="margin-top:22px">Decide what's best for you without having to deal with pushy insurance agents.</li>
    <li style="margin-top:22px">Virtual agent tools are available to help you choose what life insurance policy is best for you and your family.</li>
  </ul>
  <a class="btn" style="left:117px;top:363px;width:155px;height:41px">Compare Carriers</a>

  <svg class="abs" style="left:520px;top:70px" width="560" height="360" viewBox="520 1467 560 360">
    <defs>
      <radialGradient id="greenPhoto" cx="0.4" cy="0.35" r="0.7">
        <stop offset="0" stop-color="#a6d670"/>
        <stop offset="1" stop-color="#6fb33a"/>
      </radialGradient>
    </defs>
    <path d="M674,1504 L816,1504 M674,1790 L816,1790 M817,1644 L866,1644" stroke="rgba(255,255,255,.7)" stroke-width="1.5" fill="none"/>
    <circle cx="674" cy="1647" r="143" fill="var(--white)"/>
    <circle cx="674" cy="1647" r="121" fill="url(#greenPhoto)" role="img" aria-label="Photo of a smiling woman, tinted green"/>
    <circle cx="706" cy="1512" r="9" fill="var(--blue)"/>
    <circle cx="706" cy="1768" r="9" fill="var(--blue)"/>
    <text x="674" y="1660" text-anchor="middle" font-family="Poppins, sans-serif" font-weight="300" font-size="36" fill="#ffffff">CoverLantern</text>
  </svg>

  <div class="quote-card" style="left:816px;top:78px">
    <div class="name">Northvale</div>
    <div class="terms">$2,000,000 Death Benefit<br>20 Year Level Term<div class="price"><sup>$</sup>18<sup>.08</sup><small>/MO</small></div></div>
  </div>
  <div class="quote-card" style="left:866px;top:209px">
    <div class="name">Steadfast</div>
    <div class="terms">$2,000,000 Death Benefit<br>20 Year Level Term<div class="price"><sup>$</sup>21<sup>.17</sup><small>/MO</small></div></div>
  </div>
  <div class="quote-card" style="left:816px;top:332px">
    <div class="name">Harborly</div>
    <div class="terms">$2,000,000 Death Benefit<br>20 Year Level Term<div class="price"><sup>$</sup>23<sup>.28</sup><small>/MO</small></div></div>
  </div>
</section>

<svg class="abs" style="left:160px;top:1900px" width="440" height="440" viewBox="0 0 440 440">
  <defs>
    <linearGradient id="robotArt" x1="0" y1="0.2" x2="1" y2="0.8">
      <stop offset="0" stop-color="#8a7c6c"/>
      <stop offset="0.4" stop-color="#b9b6b0"/>
      <stop offset="0.7" stop-color="#6d9bc4"/>
      <stop offset="1" stop-color="#3a4a5c"/>
    </linearGradient>
  </defs>
  <path d="M150,60 C200,30 260,50 310,60 C360,70 370,120 350,160 C330,200 350,260 330,320 C310,380 260,420 220,410 C180,400 140,330 130,260 C120,180 100,100 150,60 Z" fill="var(--green)"/>
  <path role="img" aria-label="Illustration of a robot head with headphones and a glowing digital burst" d="M60,90 C90,50 170,40 240,60 C300,80 320,140 330,200 C340,270 320,340 260,370 C200,400 120,380 80,340 C40,300 10,250 20,190 C25,150 40,115 60,90 Z" fill="url(#robotArt)" stroke="var(--white)" stroke-width="6"/>
  <circle cx="96" cy="42" r="11" fill="var(--blue)"/>
  <circle cx="120" cy="12" r="4" fill="var(--blue)"/>
  <circle cx="347" cy="363" r="10" fill="var(--blue)"/>
  <circle cx="198" cy="408" r="15" fill="var(--blue)"/>
  <circle cx="160" cy="398" r="8" fill="var(--blue)"/>
</svg>
<h2 class="section-title" style="left:598px;top:2010px">VIRTUAL AGENT</h2>
<ul class="ticks" style="left:598px;top:2056px;width:400px">
  <li>Our Virtual Agent Lumi can help you calculate how much death benefit you need.</li>
  <li style="margin-top:22px">Lumi can help you figure out what type of Life Insurance is right for you and your family.</li>
  <li style="margin-top:22px">Lumi can evaluate your health history and provide you with accurate quotes.</li>
</ul>
<a class="btn blue" style="left:598px;top:2253px;width:155px;height:42px">Virtual Agent</a>

<section class="live-band">
  <h2 class="section-title" style="left:212px;top:94px">LIVE AGENT SUPPORT</h2>
  <ul class="ticks" style="left:212px;top:140px;width:400px">
    <li style="font-size:14.5px">If you need a Live Agent, CoverLantern has you covered.&nbsp; Our CoverLantern Agents are not paid a commission. So if you have questions our agents have the answers that best suit your needs.</li>
    <li style="margin-top:20px;font-size:14.5px">Call Toll Free: 1-888-555-0142</li>
    <li style="margin-top:20px;font-size:14.5px">Email: Info@CoverLantern.com</li>
  </ul>
  <a class="btn" style="left:212px;top:331px;width:167px;height:42px">Live Agent Support</a>
  <svg class="abs" style="left:640px;top:60px" width="360" height="350" viewBox="0 0 360 350">
    <defs>
      <linearGradient id="agentPhoto" x1="0" y1="0" x2="1" y2="1">
        <stop offset="0" stop-color="#c7ccd2"/>
        <stop offset="0.45" stop-color="#e9d3c4"/>
        <stop offset="0.7" stop-color="#d7b3a0"/>
        <stop offset="1" stop-color="#f3f1ee"/>
      </linearGradient>
    </defs>
    <circle cx="179" cy="174" r="172" fill="var(--blue)"/>
    <circle cx="165" cy="170" r="157" fill="var(--white)"/>
    <circle cx="165" cy="170" r="150" fill="url(#agentPhoto)" role="img" aria-label="Photo of a smiling customer support agent wearing a headset"/>
  </svg>
</section>

<svg class="abs" style="left:200px;top:2895px" width="420" height="340" viewBox="0 0 420 340">
  <defs>
    <linearGradient id="laptopPhoto" x1="0" y1="1" x2="1" y2="0">
      <stop offset="0" stop-color="#cfc6b8"/>
      <stop offset="0.4" stop-color="#9a9590"/>
      <stop offset="0.7" stop-color="#e6e8ea"/>
      <stop offset="1" stop-color="#5e6064"/>
    </linearGradient>
  </defs>
  <path d="M40,100 C70,60 140,70 200,55 C280,35 360,40 395,110 C420,170 410,220 385,250 C360,280 320,220 280,230 C200,250 120,220 80,190 C40,160 20,130 40,100 Z" fill="var(--blue)"/>
  <path role="img" aria-label="Photo of a person typing on a laptop showing an application submitted confirmation" d="M60,125 C80,60 160,18 240,12 C320,8 360,70 358,150 C356,240 300,290 220,292 C140,294 70,260 48,210 C38,180 50,150 60,125 Z" fill="url(#laptopPhoto)" stroke="var(--white)" stroke-width="6"/>
  <circle cx="113" cy="42" r="15" fill="var(--green)"/>
  <circle cx="142" cy="18" r="6" fill="var(--green)"/>
  <circle cx="346" cy="250" r="10" fill="var(--green)"/>
  <circle cx="253" cy="313" r="12" fill="var(--green)"/>
</svg>
<h2 class="section-title" style="left:640px;top:2950px">APPLY ONLINE</h2>
<ul class="ticks" style="left:640px;top:2986px;width:400px">
  <li>Pick your policy and apply online in minutes.</li>
  <li style="margin-top:22px">Secure Online Portal keeps your information safe and secure.</li>
  <li style="margin-top:22px">24/7 access to your policy documents.</li>
</ul>
<a class="btn" style="left:641px;top:3135px;width:155px;height:43px">Portal Login</a>

<svg class="footer-art" width="1200" height="590" viewBox="0 3180 1200 590">
  <path d="M0,3385 Q600,3184 1200,3385 V3770 H0 Z" fill="var(--green)"/>
  <path d="M0,3392 Q600,3236 1200,3392 V3770 H0 Z" fill="var(--blue)"/>
</svg>
<footer>
  <div class="brand" style="left:123px;top:3440px;font-size:28px">CoverLantern</div>
  <div class="footer-col" style="left:123px;top:3489px">
    <ul>
    <li style="line-height:24px"><svg width="12" height="14" viewBox="0 0 12 14" style="top:5px"><path d="M6,1 C3,1 1.5,3.2 1.5,5.5 C1.5,8.5 6,13 6,13 C6,13 10.5,8.5 10.5,5.5 C10.5,3.2 9,1 6,1 Z" fill="none" stroke="#fff" stroke-width="1.5"/><circle cx="6" cy="5.5" r="1.6" fill="#fff"/></svg>4820 Harbor Point Road,<br>Suite 310 Lakeview,<br>FL 30118</li>
    </ul>
  </div>
  <span class="social" style="left:121px"></span>
  <span class="social" style="left:160px"></span>
  <span class="social" style="left:202px"></span>
  <span class="social" style="left:246px"></span>

  <div class="footer-col" style="left:361px;top:3447px">
    <h4>life Insurance Products</h4>
    <ul>
      <li><svg width="12" height="12"><circle cx="6" cy="6" r="6" fill="#fff"/><path d="M3.3,6.2 L5.2,8 L8.8,4.2" stroke="var(--blue)" stroke-width="1.6" fill="none"/></svg>10 Year Level Team</li>
      <li><svg width="12" height="12"><circle cx="6" cy="6" r="6" fill="#fff"/><path d="M3.3,6.2 L5.2,8 L8.8,4.2" stroke="var(--blue)" stroke-width="1.6" fill="none"/></svg>15 Year Level Team</li>
      <li><svg width="12" height="12"><circle cx="6" cy="6" r="6" fill="#fff"/><path d="M3.3,6.2 L5.2,8 L8.8,4.2" stroke="var(--blue)" stroke-width="1.6" fill="none"/></svg>20 Year Level Team</li>
      <li><svg width="12" height="12"><circle cx="6" cy="6" r="6" fill="#fff"/><path d="M3.3,6.2 L5.2,8 L8.8,4.2" stroke="var(--blue)" stroke-width="1.6" fill="none"/></svg>30 Year Level Team</li>
      <li><svg width="12" height="12"><circle cx="6" cy="6" r="6" fill="#fff"/><path d="M3.3,6.2 L5.2,8 L8.8,4.2" stroke="var(--blue)" stroke-width="1.6" fill="none"/></svg>10 Year Level Team</li>
    </ul>
  </div>

  <div class="footer-col" style="left:647px;top:3447px">
    <h4>Tools</h4>
    <ul>
      <li><svg width="12" height="12"><circle cx="6" cy="6" r="6" fill="#fff"/><path d="M3.3,6.2 L5.2,8 L8.8,4.2" stroke="var(--blue)" stroke-width="1.6" fill="none"/></svg>Quote Comparison</li>
      <li><svg width="12" height="12"><circle cx="6" cy="6" r="6" fill="#fff"/><path d="M3.3,6.2 L5.2,8 L8.8,4.2" stroke="var(--blue)" stroke-width="1.6" fill="none"/></svg>Secure Client Portal</li>
      <li><svg width="12" height="12"><circle cx="6" cy="6" r="6" fill="#fff"/><path d="M3.3,6.2 L5.2,8 L8.8,4.2" stroke="var(--blue)" stroke-width="1.6" fill="none"/></svg>Privacy Policy</li>
    </ul>
  </div>

  <div class="footer-col" style="left:868px;top:3447px">
    <h4>Contact</h4>
    <ul>
      <li><svg width="12" height="12" viewBox="0 0 12 12"><path d="M2.5,1 L4.5,1 L5.3,3.6 L4,4.6 C4.7,6 6,7.3 7.4,8 L8.4,6.7 L11,7.5 L11,9.5 C11,10.4 10.3,11 9.5,11 C5,10.7 1.3,7 1,2.5 C1,1.7 1.6,1 2.5,1 Z" fill="#fff"/></svg>1-888-555-0142</li>
      <li><svg width="13" height="10" viewBox="0 0 13 10"><rect x="0.5" y="0.5" width="12" height="9" rx="1" fill="#fff"/><path d="M1,1 L6.5,5.5 L12,1" stroke="var(--blue)" stroke-width="1.2" fill="none"/></svg>Info@CoverLantern.com</li>
      <li style="line-height:26px;margin-top:4px"><svg width="12" height="12" style="top:7px"><circle cx="6" cy="6" r="6" fill="#fff"/><path d="M3.3,6.2 L5.2,8 L8.8,4.2" stroke="var(--blue)" stroke-width="1.6" fill="none"/></svg>Monday - Friday<br>9:00 AM - 8:00 PM</li>
    </ul>
  </div>

  <div class="footer-rule"></div>
  <p class="copyright">Copyright 2022 CoverLantern. All Rights Reserved</p>
</footer>

</body>
</html>
```